KORVELTA Corporate Business Card

Modern business card design for company which focuses in the areas of Staffing, IT Consulting & Data Services. Please note: We are no longer using the IT subscript on the logo. All designs should have IT subscript removed.
Website: www.korveltait.example

```html
<!DOCTYPE html>
<html lang="en">
<head>
<meta charset="utf-8">
<title>KORVELTA Business Card</title>
<link href="https://fonts.googleapis.com/css2?family=Montserrat:wght@400;700&family=Oswald:wght@500&display=swap" rel="stylesheet">
<style>
  :root {
    --backdrop: #232323;
    --card: #1a1a1a;
    --accent: #1e9be0;
    --text: #f2f2f2;
  }
  html, body {
    margin: 0;
    width: 1200px;
    height: 900px;
    overflow: hidden;
    background: var(--backdrop);
    font-family: "Montserrat", sans-serif;
  }
  .stage {
    width: 1200px;
    height: 900px;
    display: flex;
    flex-direction: column;
    align-items: center;
    justify-content: center;
    gap: 40px;
  }
  .card {
    position: relative;
    width: 640px;
    height: 366px;
    background: var(--card);
    border-bottom: 5px solid var(--accent);
    box-sizing: border-box;
    box-shadow: 0 10px 30px rgba(0,0,0,.45);
  }
  .brand {
    display: flex;
    align-items: center;
    gap: 14px;
    color: var(--accent);
    font-weight: 700;
    letter-spacing: 2px;
  }
  .brand-mark {
    width: 0.8em;
    height: 0.8em;
    background: var(--accent);
    border-radius: 4px;
  }
  .card--front .brand {
    position: absolute;
    top: 50%;
    left: 50%;
    transform: translate(-50%, -50%);
    font-size: 52px;
  }
  .card--back .brand {
    position: absolute;
    top: 56px;
    left: 50%;
    transform: translateX(-50%);
    font-size: 44px;
  }
  .person {
    position: absolute;
    top: 168px;
    left: 50px;
    width: 230px;
    text-align: right;
  }
  .person-name {
    font-family: "Oswald", sans-serif;
    font-weight: 500;
    font-size: 36px;
    color: var(--accent);
    letter-spacing: 1px;
    text-transform: uppercase;
    line-height: 1;
  }
  .person-title {
    margin-top: 6px;
    font-size: 15px;
    color: var(--text);
    letter-spacing: 1px;
  }
  .divider {
    position: absolute;
    top: 166px;
    left: 306px;
    width: 2px;
    height: 72px;
    background: var(--accent);
  }
  .contacts {
    position: absolute;
    top: 164px;
    left: 330px;
    margin: 0;
    padding: 0;
    list-style: none;
    color: var(--text);
    font-size: 15px;
    line-height: 26px;
  }
  .contacts li {
    display: flex;
    align-items: center;
    gap: 10px;
  }
  .contacts svg {
    width: 13px;
    height: 13px;
    flex: none;
  }
  .address {
    position: absolute;
    bottom: 38px;
    left: 0;
    right: 0;
    text-align: center;
    color: var(--text);
    font-size: 15px;
    letter-spacing: 0.5px;
  }
</style>
</head>
<body>
<main class="stage">
  <section class="card card--front">
    <div class="brand"><span class="brand-mark"></span>KORVELTA</div>
  </section>

  <section class="card card--back">
    <div class="brand"><span class="brand-mark"></span>KORVELTA</div>

    <div class="person">
      <div class="person-name">Daniel Archer</div>
      <div class="person-title">Director</div>
    </div>

    <div class="divider"></div>

    <ul class="contacts">
      <li>
        <svg viewBox="0 0 16 16" aria-hidden="true"><path d="M4 1l3 3-2 2c1 2 3 4 5 5l2-2 3 3-2 2C7 14 2 9 2 3z" fill="var(--accent)"/></svg>
        555-014-2290
      </li>
      <li>
        <svg viewBox="0 0 16 16" aria-hidden="true"><rect x="1.5" y="3.5" width="13" height="9" fill="none" stroke="var(--accent)" stroke-width="1.5"/><path d="M1.5 3.5l6.5 5 6.5-5" fill="none" stroke="var(--accent)" stroke-width="1.5"/></svg>
        contactus@korveltait.example
      </li>
      <li>
        <svg viewBox="0 0 16 16" aria-hidden="true"><circle cx="8" cy="8" r="6.5" fill="none" stroke="var(--accent)" stroke-width="1.4"/><ellipse cx="8" cy="8" rx="3" ry="6.5" fill="none" stroke="var(--accent)" stroke-width="1.2"/><path d="M1.5 8h13" stroke="var(--accent)" stroke-width="1.2"/></svg>
        www.korveltait.example
      </li>
    </ul>

    <div class="address">418 Harlow St. Brentonville, IN 46010</div>
  </section>
</main>
</body>
</html>
```